Loftera- Attic Storage and Skylights.

Hi,Would would like to have a noticeable design for a full wrap on our big van. The van is a Brevik Haulmaster LWB. Very important that our message is clear as to what we do. We want the design to be very noticeable with the use of 2/3 colours. Am open to using imagery of our work. Please see the attached logo we have for a colour scheme and an example image if someone would like to place an image on the van- It's not critical.Thanks,Loftera
Target Market(s)
We are geared toward 30+ male and female homeowners.
Industry/Entity Type
Residential Construction
Requirements
Must have
- Clear visual of our logo with a website www.loftera.com.au
- We need our contact details on the van along with the signs for social media. We want to give the impression we are a successful trusted business.
Should not have
- Do not what huge amounts of white in the design. Would like our colours to be based around our logo.

```html
<!DOCTYPE html>
<html lang="en">
<head>
<meta charset="utf-8">
<title>Loftera – Van Wrap Layout</title>
<link rel="stylesheet" href="https://fonts.googleapis.com/css2?family=Lato:wght@700;900&family=Montserrat:wght@400;600;700&display=swap">
<style>
  :root {
    --canvas-bg: #262626;
    --brand-blue: #1b6fbd;
    --brand-navy: #2b3440;
    --wrap-white: #ffffff;
    --cut-line: #e0202a;
    --photo-light: #ece7df;
    --photo-mid: #c9bfb0;
    --photo-dark: #6a5a48;
  }
  html, body {
    margin: 0;
    padding: 0;
    width: 1200px;
    height: 1080px;
    overflow: hidden;
    background: var(--canvas-bg);
  }
  .wrap-layout {
    position: absolute;
    left: 0;
    top: 328px;
    width: 1200px;
    height: 423px;
    display: block;
  }
  .headline { font-family: "Lato", sans-serif; font-weight: 900; }
  .tagline { font-family: "Lato", sans-serif; font-weight: 700; }
  .brand-name { font-family: "Montserrat", sans-serif; font-weight: 600; }
  .service-list { font-family: "Montserrat", sans-serif; font-weight: 700; }
  .web-address { font-family: "Montserrat", sans-serif; font-weight: 400; }
</style>
</head>
<body>
<svg class="wrap-layout" viewBox="60 820 1390 490" xmlns="http://www.w3.org/2000/svg" aria-label="Loftera van side wrap layout">
  <defs>
    <clipPath id="van-body-clip">
      <path d="M75,1205 L76,1190 Q80,1150 110,1140 L170,1125 Q195,1118 215,1100 L440,880 Q470,850 530,845 L700,838 L1385,836 Q1410,840 1412,865 L1422,1075 L1400,1085 L1396,1195 L1388,1200 L1195,1200 Q1180,1170 1140,1168 Q1098,1170 1085,1200 L330,1200 Q312,1178 272,1178 Q232,1180 218,1205 Z"/>
    </clipPath>
    <linearGradient id="photo-tones" x1="0" y1="0" x2="0.3" y2="1">
      <stop offset="0" stop-color="var(--photo-light)"/>
      <stop offset="0.6" stop-color="var(--photo-mid)"/>
      <stop offset="1" stop-color="var(--photo-dark)"/>
    </linearGradient>
  </defs>

  <g class="van-body" clip-path="url(#van-body-clip)">
    <rect class="body-base" x="60" y="820" width="1400" height="420" fill="var(--wrap-white)"/>
    <polygon class="top-dark-wedge" points="470,830 1460,830 1460,880 1140,992 500,852" fill="var(--brand-navy)"/>
    <polygon class="phone-strip" points="850,878 1165,935 1150,990 835,935" fill="var(--brand-blue)"/>
    <polygon class="lower-blue" points="60,1140 150,1125 285,1098 500,1000 560,992 1460,1205 1460,1240 60,1240" fill="var(--brand-blue)"/>
    <polygon class="headline-band" points="505,1010 560,1004 1200,1158 1190,1215 505,1055" fill="var(--brand-navy)"/>
    <path class="work-photo" d="M1205,830 Q1090,1020 1175,1210 L1460,1210 L1460,830 Z" fill="url(#photo-tones)" role="img" aria-label="Photo of a finished attic storage room with skylight and timber floor"/>
    <path class="photo-frame" d="M1205,830 Q1090,1020 1175,1210" fill="none" stroke="var(--brand-navy)" stroke-width="12"/>
  </g>

  <path class="cut-outline" d="M75,1205 L76,1190 Q80,1150 110,1140 L170,1125 Q195,1118 215,1100 L440,880 Q470,850 530,845 L700,838 L1385,836 Q1410,840 1412,865 L1422,1075 L1400,1085 L1396,1195 L1388,1200 L1195,1200 Q1180,1170 1140,1168 Q1098,1170 1085,1200 L330,1200 Q312,1178 272,1178 Q232,1180 218,1205 Z" fill="none" stroke="var(--cut-line)" stroke-width="1.5"/>

  <path class="cab-window" d="M280,1100 L420,968 Q460,940 512,935 Q522,937 520,948 L516,1080 Q514,1098 495,1100 Z" fill="var(--canvas-bg)" stroke="var(--cut-line)" stroke-width="1.5"/>

  <g class="door-handles" fill="var(--brand-navy)" stroke="var(--cut-line)" stroke-width="1.5">
    <rect x="470" y="1106" width="46" height="8" rx="4"/>
    <rect x="558" y="1106" width="46" height="8" rx="4"/>
  </g>

  <g class="contact-block">
    <circle class="phone-badge" cx="826" cy="882" r="32" fill="var(--wrap-white)"/>
    <path class="phone-badge-tail" d="M804,902 L797,918 L816,909 Z" fill="var(--wrap-white)"/>
    <path class="phone-icon" d="M815,869 q4,-3 7,0 l4,6 q2,3 -1,6 l-3,2 q3,7 10,11 l2,-3 q3,-3 6,-1 l6,4 q3,3 0,7 l-3,3 q-6,5 -18,-4 q-12,-10 -13,-21 q0,-6 3,-10 z" fill="var(--brand-blue)"/>
    <path d="M831,865 a14,14 0 0 1 14,14 M831,858 a21,21 0 0 1 21,21" fill="none" stroke="var(--brand-blue)" stroke-width="2.5"/>
    <g transform="rotate(11 946 868)">
      <text class="headline" x="946" y="868" font-size="22" fill="var(--wrap-white)" textLength="168" lengthAdjust="spacingAndGlyphs">CALL NOW ON</text>
    </g>
    <g transform="rotate(11 872 905)">
      <text class="headline" x="872" y="905" font-size="36" fill="var(--wrap-white)" textLength="240" lengthAdjust="spacingAndGlyphs">1300 64 18 27</text>
    </g>
  </g>

  <g class="brand-lockup" transform="rotate(12.5 640 990)">
    <rect x="640" y="944" width="40" height="40" fill="var(--brand-blue)"/>
    <text class="brand-name" x="696" y="984" font-size="62" fill="var(--brand-navy)" textLength="400" lengthAdjust="spacingAndGlyphs">LOFTERA</text>
  </g>

  <g transform="rotate(13.5 570 1052)">
    <text class="headline" x="570" y="1052" font-size="46" fill="var(--wrap-white)" textLength="555" lengthAdjust="spacingAndGlyphs">HOME STORAGE EXPERTS.</text>
  </g>
  <g transform="rotate(13.5 614 1115)">
    <text class="tagline" x="614" y="1115" font-size="24" fill="var(--wrap-white)" textLength="330" lengthAdjust="spacingAndGlyphs">ROOM TO GROW.....UPWARD.</text>
  </g>

  <g class="service-list" font-size="17" fill="var(--wrap-white)">
    <text x="310" y="1121">• ATTIC ROOMS</text>
    <text x="310" y="1141">• ATTIC LADDERS</text>
    <text x="310" y="1161">• ATTIC STORAGE</text>
    <text x="310" y="1181">• SKYLIGHTS</text>
  </g>

  <g class="sill-panels" fill="var(--brand-blue)" stroke="var(--cut-line)" stroke-width="1.5">
    <path d="M350,1243 L1053,1243 L1043,1295 L358,1295 Z"/>
    <path d="M1205,1243 L1370,1243 L1366,1285 L1212,1285 Z"/>
  </g>
  <text class="web-address" x="502" y="1280" font-size="20" fill="var(--wrap-white)" textLength="386" lengthAdjust="spacing">WWW.LOFTERA.COM.AU</text>
</svg>
</body>
</html>
```